Accounting firm needing business card / letterhead designed
Marcus T. Elbering, CPA
marcus@fernquill.com
www.fernquill.com
482 N Harlow Ave Larkfield, OH 43719
419-555-0172

```html
<!DOCTYPE html>
<html lang="en">
<head>
<meta charset="utf-8">
<title>Fernquill Business Card</title>
<link href="https://fonts.googleapis.com/css2?family=Oswald:wght@300;500&family=Mulish:wght@400;700&display=swap" rel="stylesheet">
<style>
  :root {
    --backdrop: #2d3039;
    --paper: #ffffff;
    --navy: #241f5e;
    --violet: #4f4a8c;
    --green: #8dc63f;
    --ink: #3a3a3a;
  }
  * { margin: 0; padding: 0; box-sizing: border-box; }
  html, body {
    width: 1200px; height: 640px; overflow: hidden;
    background: var(--backdrop);
    font-family: "Mulish", Arial, sans-serif;
  }
  .card {
    position: absolute;
    top: 184px;
    width: 411px; height: 230px;
    background: var(--paper);
    box-shadow: 0 2px 0 #111, 0 4px 10px rgba(0,0,0,.35);
    overflow: hidden;
  }
  .card--front { left: 178px; }
  .card--back { left: 610px; }

  .brand {
    position: absolute;
    font-family: "Mulish", Arial, sans-serif;
    font-weight: 700;
    color: var(--violet);
    letter-spacing: 1px;
    text-transform: uppercase;
    white-space: nowrap;
    transform: translateX(-50%);
  }
  .card--front .brand { left: 98px; top: 112px; font-size: 19px; }
  .card--back .brand { left: 206px; top: 96px; font-size: 30px; }

  .divider { position: absolute; left: 0; top: 0; }

  .person { position: absolute; left: 231px; top: 36px; color: var(--navy); }
  .person__name {
    font-family: "Oswald", "Arial Narrow", sans-serif;
    font-weight: 300; font-size: 15px; letter-spacing: .2px;
    text-transform: uppercase; line-height: 18px;
  }
  .person__name strong { font-weight: 500; }
  .person__title { font-size: 7.5px; letter-spacing: .5px; }

  .contact { position: absolute; left: 231px; list-style: none; }
  .contact--main { top: 104px; }
  .contact--address { top: 198px; }
  .contact li {
    display: flex; align-items: center; gap: 7px;
    height: 17px; font-size: 8px; color: var(--ink); white-space: nowrap;
  }
  .contact svg { width: 9px; height: 9px; flex: none; }

  .rule-dashed { position: absolute; left: 231px; top: 178px; }

  .back-url {
    position: absolute; left: 0; right: 0; top: 193px;
    text-align: center; font-size: 8px; color: var(--ink);
  }
  .back-band { position: absolute; left: 0; bottom: 0; }
</style>
</head>
<body>

<section class="card card--front">
  <div class="brand">Fernquill</div>

  <svg class="divider" width="411" height="230" viewBox="0 0 411 230" aria-hidden="true">
    <polygon points="200,0 205,0 205,35 200,30" fill="var(--navy)"/>
    <rect x="200" y="99" width="5" height="58" fill="var(--green)"/>
    <polygon points="200,199 205,194 205,230 200,230" fill="var(--navy)"/>
  </svg>

  <div class="person">
    <div class="person__name"><strong>Marcus T.</strong> Elbering</div>
    <div class="person__title">CPA</div>
  </div>

  <ul class="contact contact--main">
    <li>
      <svg viewBox="0 0 10 10"><rect width="10" height="10" rx="2" fill="var(--green)"/><path d="M3 2.5c.4 2.4 2 4 4.5 4.6l.4-1.1-1.3-.6-.6.6C5 5.6 4.4 5 4 4l.6-.6-.6-1.3z" fill="#fff"/></svg>
      640-555-0172
    </li>
    <li>
      <svg viewBox="0 0 10 10"><rect width="10" height="10" rx="2" fill="var(--green)"/><rect x="2.3" y="3" width="5.4" height="4" fill="none" stroke="#fff" stroke-width=".8"/><path d="M2.3 3l2.7 2.2L7.7 3" fill="none" stroke="#fff" stroke-width=".8"/></svg>
      marcus@fernquill.com
    </li>
    <li>
      <svg viewBox="0 0 10 10"><rect width="10" height="10" rx="2" fill="var(--green)"/><circle cx="5" cy="5" r="2.6" fill="none" stroke="#fff" stroke-width=".8"/><path d="M2.4 5h5.2M5 2.4v5.2" stroke="#fff" stroke-width=".6"/></svg>
      www.fernquill.com
    </li>
  </ul>

  <svg class="rule-dashed" width="144" height="3" viewBox="0 0 144 3" aria-hidden="true">
    <line x1="0" y1="1.5" x2="144" y2="1.5" stroke="var(--green)" stroke-width="1.6" stroke-dasharray="3 2.6"/>
  </svg>

  <ul class="contact contact--address">
    <li>
      <svg viewBox="0 0 10 10"><rect width="10" height="10" rx="2" fill="var(--green)"/><path d="M5 8.3C3.4 6.4 2.8 5.3 2.8 4.3a2.2 2.2 0 0 1 4.4 0c0 1-.6 2.1-2.2 4z" fill="#fff"/><circle cx="5" cy="4.3" r=".8" fill="var(--green)"/></svg>
      482 N Harlow Ave Larkfield, OH 43719
    </li>
  </ul>
</section>

<section class="card card--back">
  <div class="brand">Fernquill</div>
  <div class="back-url">www.fernquill.com</div>
  <svg class="back-band" width="411" height="20" viewBox="0 0 411 20" aria-hidden="true">
    <rect width="411" height="20" fill="var(--navy)"/>
    <polygon points="160,0 252,0 250,20 162,20" fill="var(--green)"/>
  </svg>
</section>

</body>
</html>
```